Business card design for a real estate company

We need a business card design a real estate development company called "Vantrelo Holding SA" in Switzerland. Space needed for two phone numbers in international format (one is +7 (912) xxx-xx-xx, the other +41 (76) xxx-xx-xx), e-mail (mb@vantrelo.example), name, position and address of the company:
Rue des Tilleuls 24
CH-1700 Fribourg
Switzerland

Target Market(s)

Potential partners, architects, banks etc..

Industry/Entity Type

Business

Requirements
Must have
• Slight, elegant.
Should not have
• Do not include illustrations of buildings etc..

```html
<!DOCTYPE html>
<html lang="en">
<head>
<meta charset="utf-8">
<title>Vantrelo Holding SA – Business Card</title>
<link rel="stylesheet" href="https://fonts.googleapis.com/css2?family=Archivo:wght@400;700;800&display=swap">
<style>
  :root {
    --page: #ffffff;
    --card-core: #4a362a;
    --card-edge: #2f2119;
    --ink-light: #f4e9df;
    --ink-tan: #d9b59c;
    --rule: #a88a76;
  }
  * { margin: 0; padding: 0; box-sizing: border-box; }
  html, body {
    width: 1200px; height: 363px; overflow: hidden;
    background: var(--page);
    font-family: "Archivo", Arial, sans-serif;
  }
  .sheet { position: relative; width: 1200px; height: 363px; }
  .card {
    position: absolute; top: 0; height: 363px;
    background: radial-gradient(ellipse at 45% 40%, var(--card-core) 0%, var(--card-edge) 85%);
    overflow: hidden;
  }
  .card--front { left: 0; width: 584px; }
  .card--back { left: 600px; width: 600px; }
  .rule { position: absolute; background: var(--rule); }
  .wordmark {
    position: absolute; font-weight: 800; font-size: 25px;
    letter-spacing: 6px; color: var(--ink-light); white-space: nowrap;
  }
  .country {
    position: absolute; font-weight: 700; font-size: 14px;
    letter-spacing: 2.5px; color: var(--ink-light);
  }
  .card--front .wordmark { right: 20px; top: 280px; }
  .card--front .country { right: 22px; top: 313px; }
  .card--front .rule--v { left: 103px; top: 217px; width: 1px; height: 146px; }
  .card--front .rule--h { left: 103px; top: 340px; width: 481px; height: 1px; }

  .card--back .wordmark { right: 22px; top: 44px; }
  .card--back .country { right: 24px; top: 90px; }
  .card--back .rule--h { left: 0; top: 141px; width: 600px; height: 1px; }
  .card--back .rule--v { left: 34px; top: 141px; width: 1px; height: 222px; }

  .person { position: absolute; left: 61px; top: 184px; }
  .person__name { font-weight: 800; font-size: 17px; letter-spacing: 2px; color: var(--ink-light); }
  .person__role { font-weight: 700; font-size: 13px; letter-spacing: 1.5px; color: var(--ink-tan); margin-top: 6px; }

  .address { position: absolute; left: 344px; top: 184px; font-weight: 700; font-size: 14px; letter-spacing: 1.5px; line-height: 18px; }
  .address__label { color: var(--ink-tan); }
  .address__line { color: var(--ink-light); }

  .contacts {
    position: absolute; left: 22px; right: 22px; top: 328px;
    display: flex; justify-content: space-between;
    font-size: 9.5px; font-weight: 400; letter-spacing: 2px; color: var(--ink-tan);
  }
</style>
</head>
<body>
<div class="sheet">
  <section class="card card--front">
    <div class="rule rule--v"></div>
    <div class="rule rule--h"></div>
    <div class="wordmark">VantreloHoldingSA</div>
    <div class="country">Switzerland</div>
  </section>

  <section class="card card--back">
    <div class="wordmark">VantreloHoldingSA</div>
    <div class="country">Switzerland</div>
    <div class="rule rule--h"></div>
    <div class="rule rule--v"></div>

    <div class="person">
      <div class="person__name">JOHN SMITH</div>
      <div class="person__role">Director</div>
    </div>

    <div class="address">
      <div class="address__label">ADDRESS:</div>
      <div class="address__line">Rue des Tilleuls 24</div>
      <div class="address__line">CH-1700 Fribourg</div>
      <div class="address__line">Switzerland</div>
    </div>

    <div class="contacts">
      <span>PHONE: +7 (912) xxx-xx-xx</span>
      <span>+41 (76) xxx-xx-xx</span>
      <span>EMAIL: mb@vantrelo.example</span>
    </div>
  </section>
</div>
</body>
</html>
```